Web Design

We need a new website for our company. We perform several functions:

1 - IT and Network Support
2 - Computer Consultancy
3 - Cloud Services
4 - Hosted Mailvault & Online Backup
5 - Internet Connections & VOIP

Examples of some of the designs we like can be seen on:
• www.quorvex.com
• www.brintale.com

I urgently need a new website to be designed to enable me to look more professional. My competitors website is www.plmtr.co.uk

I also want to be able to look much more professional, like www.quorvex.com www.brintale.com

I have attached how I would like the website to look

Task outline
To design a home page and another internal skeleton page for a website following our requirements specification and wireframe layout/structure

Task description
We are looking for a modern, attractive, clean design for our new website to reflect our businesses professionalism and high quality services that we offer.
• www.quorvex.com
• www.brintale.com
We would like a design for a home page and one other skeleton subpage for our website. We have provided a wireframe image to assist, showing how we would like the layout/structure of our website to follow which also highlights where we would like specific content/features to go.
We have listed what features the site must have in the requirements section.
The final design should communicate to our users that we are a professional business that offer high quality services and that we are a company they can trust and rely on.

Look and feel
The wireframe we have attached is a representation of how we would like the layout and structure of the website to be designed. We would like to have a corporate theme to our website.

Colours
Open to interpretation by the designer, as long as the colours suit a corporate theme and give off a professional look and feel.

Requirements
The design must have the following:

General
• Home page design (Based on attached wireframe).
• Internal Page design (This needs to be a skeleton page which can be used for implemented the content for all over pages).

• Contact details to be visible on every page, contact number at the header and all other relative details in the footer section.
• Social networking icons within the footer section of the site.
• Avoid the use of unprofessional images for buttons, icons and banners etc.
Features desired
• Drop down navigation bar. Please see the attached image for inspiration for its design/layout.
o We would like a similar drop down menu design to the one on this site: www.plmtr.co.uk.
• Image slider at the header of every page just beneath the navigation bar.
o We would like the Talu slider to be used for the image slider. Please use this link for an example of it in action: http://www.scriptgarnet.net/demo/talu-slider/
o The image slider needs to be larger on the home page.
o The image slider can be smaller on the rest of the pages of the site.
• Chirplet feed present on every page.
• News/Blog feed present on every page.
• Call back form present on every page.
• Wendro Map implementation above footer on every page.

A user friendly, accessible design that is easy to use and easy for the user to understand. Must have a corporate theme to reflect the professionalism of our business. Content flows logically and keep content spaced out so that it does not make the site look cluttered.

Target Market(s)

Small to Mid sized Business, Large Banks and Legal, corporate, business - non-technical users

Industry/Entity Type

Business

Font styles to use
Sans Serif

```html
<!DOCTYPE html>
<html lang="en">
<head>
<meta charset="utf-8">
<title>Ferncastle Systems</title>
<link href="https://fonts.googleapis.com/css2?family=Open+Sans:wght@400;600;700;800&family=Raleway:wght@400;500;700&display=swap" rel="stylesheet">
<style>
:root{
  --blue:#1b7ccc;
  --blue-light:#4aaae8;
  --navy:#1d3f86;
  --ink:#3d4a5c;
  --muted:#8a94a2;
  --line:#e2e6ea;
  --quote:#8b9aa6;
  --bg:#ffffff;
  --foot:#f4f6f8;
}
*{margin:0;padding:0;box-sizing:border-box}
html,body{width:960px;height:1200px;overflow:hidden;background:var(--bg)}
body{position:relative;font-family:"Open Sans",Arial,sans-serif;color:var(--ink)}
.abs{position:absolute}

/* hero */
.hero-bg{left:0;top:0;width:960px;height:385px;background:linear-gradient(100deg,#2a4a8e 0%,#3c6fc0 35%,#6b9ad8 60%,#2f5fb3 100%)}
.hero-curve{left:0;top:330px;width:960px;height:60px}
.portrait{left:500px;top:86px;width:270px;height:298px;background:radial-gradient(ellipse at 50% 40%,#e9c9b2 0%,#b9d4ee 40%,rgba(120,165,220,0) 75%)}
.logo{left:197px;top:18px;display:flex;align-items:center;gap:8px;color:#fff;font-family:"Raleway",sans-serif;font-size:16px;letter-spacing:1.5px}
.logo-dot{width:12px;height:12px;border-radius:50%;background:#fff}
.contact-top{top:24px;font-size:6.5px;color:#fff;display:flex;align-items:center;gap:4px}
.btn{background:linear-gradient(#55b4ee,#2188d4);color:#fff;font-weight:600;border:1px solid #8fd0f7;border-radius:2px;display:flex;align-items:center;justify-content:center}
.btn-touch{left:677px;top:14px;width:83px;height:26px;font-size:9px}
.nav{left:198px;top:57px;width:564px;height:29px;background:linear-gradient(#fbfbfb,#e3e5e8);border-radius:2px;display:flex;align-items:center;font-size:7.5px;font-weight:600;color:#4d5563}
.nav a{text-decoration:none;color:inherit;padding:0 10px}
.nav .current{background:linear-gradient(#5ab6ee,#2b8cd6);color:#fff;height:29px;width:54px;margin-left:5px;margin-right:6px;display:flex;align-items:center;justify-content:center;padding:0}
.hero-kicker{left:201px;top:128px;color:#fff;font-family:"Raleway",sans-serif;font-size:14px}
.hero-title{left:201px;top:145px;color:#fff;font-family:"Raleway",sans-serif;font-weight:700;font-size:25px}
.hero-copy{left:201px;top:184px;width:250px;color:#fff;font-size:9.5px;line-height:15.5px}
.btn-hero{left:202px;top:255px;width:84px;height:26px;font-size:8.5px}
.arrow{top:217px;width:36px;height:36px;background:rgba(20,30,50,.65);display:flex;align-items:center;justify-content:center}
.dots{left:204px;top:339px;display:flex;gap:5px;align-items:center}
.dots span{width:6px;height:6px;border-radius:50%;background:#fff}
.dots .on{width:8px;height:8px;background:var(--blue-light);border:1.5px solid #fff}

/* service tiles */
.tile{width:180px;height:106px;border-radius:2px;color:#fff;padding:14px 12px}
.tile h3{font-size:13.5px;font-weight:800;letter-spacing:-.6px;margin-bottom:3px}
.tile p{font-size:6.6px;line-height:10.8px;letter-spacing:-.2px}
.tile .more{position:absolute;right:16px;bottom:12px;width:48px;height:18px;font-size:6px}
.t-backup{background:linear-gradient(135deg,#5d7fb8,#2a3f6e)}
.t-onsite{background:linear-gradient(135deg,#3e5c7a,#6a4a8a)}
.t-remote{background:linear-gradient(135deg,#4f6ea8,#1f2e58)}
.t-mail{background:linear-gradient(135deg,#8a5a32,#3b2a22)}

/* content */
.welcome{left:198px;top:642px;font-family:"Raleway",sans-serif;font-size:18.5px;color:#4a5568}
.about{left:198px;top:677px;width:374px;font-size:6.7px;line-height:10.8px;color:#4a5260}
.h-test{left:198px;top:763px;font-family:"Raleway",sans-serif;font-size:13.5px;color:#4a5568}
.person{top:792px;display:flex;gap:10px}
.avatar{width:30px;height:30px;background:linear-gradient(#c9a58b,#8a6e5e)}
.person b{display:block;font-family:"Raleway",sans-serif;font-weight:500;font-size:10.5px;color:#3d4a5c}
.person small{font-size:6.5px;color:var(--muted)}
.quote{top:834px;width:150px;height:65px;background:var(--quote);color:#fff;font-size:7px;line-height:14px;padding:9px 10px 0 29px}
.quote::before{content:"\201C";position:absolute;left:9px;top:4px;font-size:20px;font-weight:700;font-family:Georgia,serif}
.quote::after{content:"";position:absolute;left:10px;top:-6px;border:6px solid transparent;border-top:0;border-bottom-color:var(--quote)}
.badge{background:#dfe2e6;border-radius:2px}

/* sidebar */
.panel{background:#fff;border:1px solid #eceff2;box-shadow:0 1px 3px rgba(0,0,0,.05)}
.panel-head{background:var(--blue);color:#fff;font-size:10px;font-weight:600;display:flex;align-items:center;gap:7px;padding-left:14px}
.form-intro{left:601px;top:447px;font-size:6.7px;line-height:10.5px;color:var(--muted)}
.form-intro strong{color:var(--blue);font-weight:400}
.field{left:600px;width:144px;height:21px;border:1px solid var(--line);font-size:6.6px;color:#a4acb6;padding:6px 7px}
.btn-submit{left:681px;top:625px;width:63px;height:19px;background:var(--blue);color:#fff;font-size:7px;font-weight:600;display:flex;align-items:center;justify-content:center}
.tw-avatar{left:599px;top:717px;width:30px;height:30px;background:var(--blue);border:1px solid #cfe3f4}
.tw-name{left:637px;top:721px;font-size:8.5px;color:#4a5260}
.tw-handle{left:637px;top:735px;font-size:6.5px;color:#b0b8c2}
.tw-text{left:599px;top:765px;width:149px;font-size:6.7px;line-height:13px;color:#a7afb8;text-align:justify;border-top:1px solid #eef0f2;padding-top:0}
.tw-text span{color:var(--blue)}
.post{left:599px;display:flex;gap:10px}
.post .thumb{width:32px;height:32px;background:linear-gradient(135deg,#7b8797,#3f4a58)}
.post p{font-size:6.7px;line-height:12px;color:var(--muted)}
.post p b{display:block;color:#4a5260;font-weight:600;font-size:6.3px}

/* map + footer */
.map{left:0;top:1043px;width:960px;height:129px;background:linear-gradient(90deg,#e8e6df,#ecebe6 50%,#e6e5de)}
.footer{left:0;top:1172px;width:960px;height:28px;background:var(--foot);font-size:6.5px;color:#9aa3ae}
</style>
</head>
<body>

<!-- hero -->
<div class="abs hero-bg" role="img" aria-label="Blurred server room backdrop in deep blue tones"></div>
<div class="abs portrait" role="img" aria-label="Smiling IT consultant holding a laptop"></div>
<svg class="abs hero-curve" viewBox="0 0 960 60" preserveAspectRatio="none"><path d="M0 8 Q480 75 960 8 L960 60 L0 60 Z" fill="#fff"/></svg>

<div class="abs logo"><span class="logo-dot"></span>Ferncastle Systems</div>
<div class="abs contact-top" style="left:471px">
  <svg width="14" height="9" viewBox="0 0 14 9"><rect x="2" y=".5" width="11" height="8" fill="none" stroke="#fff"/><path d="M2 .5 7.5 5 13 .5" fill="none" stroke="#fff"/></svg>
  info@ferncastlesystems.com
</div>
<div class="abs contact-top" style="left:591px">
  <svg width="9" height="9" viewBox="0 0 10 10"><path d="M2 1 4 1 5 3.5 3.6 4.6Q4.8 6.8 6.4 6.4L7.5 5 10 6 10 8Q9 10 6 9 1 7 1 2Z" fill="#fff"/></svg>
  +44 100 555 0123
</div>
<div class="abs btn btn-touch">Get in Touch</div>

<nav class="abs nav">
  <a class="current" href="#">Home</a><a href="#">Company</a><a href="#">IT Support</a><a href="#">Cloud Services</a><a href="#">Partners</a><a href="#">Contact</a>
</nav>

<div class="abs hero-kicker">We Always Bring</div>
<h1 class="abs hero-title">Businesses Forward.</h1>
<p class="abs hero-copy">Lorem ipsum dolor sit amet, consectetur adipisicing elit, sed do eiusmod tempor incididunt ut labore et dolore magna. aliqua.</p>
<div class="abs btn btn-hero">Contact Us</div>

<div class="abs arrow" style="left:92px"><svg width="8" height="12" viewBox="0 0 8 12"><path d="M6 1 1.5 6 6 11" fill="none" stroke="#fff" stroke-width="1.6"/></svg></div>
<div class="abs arrow" style="left:825px"><svg width="8" height="12" viewBox="0 0 8 12"><path d="M2 1 6.5 6 2 11" fill="none" stroke="#fff" stroke-width="1.6"/></svg></div>
<div class="abs dots"><span></span><span class="on"></span><span></span><span></span></div>

<!-- services -->
<div class="abs tile t-backup" style="left:198px;top:406px" role="img" aria-label="Server racks photo">
  <h3>ONLINE BACKUP</h3>
  <p>- Protect your valuable data securely offsite.<br>- Instant Recovery.<br>- Unlimited Data Plans</p>
  <div class="btn more">Read More</div>
</div>
<div class="abs tile t-onsite" style="left:390px;top:406px" role="img" aria-label="Engineer at network cabinet photo">
  <h3>ONSITE IT SUPPORT</h3>
  <p>- No Travel or Call Out Charge.<br>- Vantrel and Norcade Engineers 24/7.<br>- Fixed Cost Repairs.</p>
  <div class="btn more">Read More</div>
</div>
<div class="abs tile t-remote" style="left:198px;top:524px" role="img" aria-label="Office monitors photo">
  <h3>REMOTE IT SUPPORT</h3>
  <p>- Anyplace, Anytime - we fix YOUR issues.<br>- Experts on-call 24/7.<br>- Fixed Costs.</p>
  <div class="btn more">Read More</div>
</div>
<div class="abs tile t-mail" style="left:390px;top:524px" role="img" aria-label="Network cables photo">
  <h3>HOSTED MAILVAULT</h3>
  <p>- Throw out your Email server!<br>- Let Us Manage your Email!<br>- Plans from £5.95 a month.</p>
  <div class="btn more">Read More</div>
</div>

<h2 class="abs welcome">Welcome to Ferncastle System</h2>
<p class="abs about">For many companies today, IT support is a large part of doing business. It is not always possible for a company or business to have a dedicated IT support team. For companies/businesses in Glasgow, Scotland, the answer for IT needs is Ferncastle Systems Limited. With Ferncastle Systems Limited, a client has the full expertise of a highly skilled team of network and infrastructure engineers to monitor and manage their network. Not only do the IT consultants of Ferncastle Systems Limited troubleshoot issues as they arise, but they also go the extra step of forecasting and assessing the risks of the network infrastructure.</p>

<h2 class="abs h-test">Client Testimonials</h2>
<div class="abs person" style="left:199px"><div class="avatar" role="img" aria-label="Client portrait"></div><div><b>Jenny Doe</b><small>Analyst</small></div></div>
<div class="abs person" style="left:390px"><div class="avatar" role="img" aria-label="Client portrait"></div><div><b>Owen Harlow</b><small>Businessman</small></div></div>
<div class="abs quote" style="left:199px">Mauris urnaei elit, mattis non urna acem, ullamcorper vula putatem lorem.</div>
<div class="abs quote" style="left:390px">Mauris urnaei elit, mattis non urna acem, ullamcorper vula putatem lorem.</div>

<!-- partner badges -->
<div class="abs badge" style="left:198px;top:934px;width:54px;height:33px"></div>
<div class="abs badge" style="left:265px;top:934px;width:44px;height:30px"></div>
<div class="abs badge" style="left:320px;top:934px;width:42px;height:30px"></div>
<div class="abs badge" style="left:374px;top:934px;width:62px;height:30px"></div>
<div class="abs badge" style="left:445px;top:936px;width:54px;height:26px"></div>
<div class="abs badge" style="left:511px;top:933px;width:32px;height:35px"></div>
<div class="abs badge" style="left:282px;top:983px;width:56px;height:32px"></div>
<div class="abs badge" style="left:348px;top:983px;width:50px;height:34px"></div>
<div class="abs badge" style="left:410px;top:985px;width:76px;height:30px"></div>

<!-- callback form -->
<div class="abs panel" style="left:585px;top:405px;width:174px;height:256px"></div>
<div class="abs panel-head" style="left:585px;top:405px;width:174px;height:28px">
  <svg width="11" height="8" viewBox="0 0 11 8"><rect x=".5" y=".5" width="10" height="7" fill="none" stroke="#fff"/><path d="M.5 .5 5.5 4.5 10.5 .5" fill="none" stroke="#fff"/></svg>
  We'd love to hear from you.
</div>
<p class="abs form-intro">We guarantee to respond within one hour<br>Alternatively call us on: <strong>0100 555 0187</strong>.</p>
<div class="abs field" style="top:481px">Name</div>
<div class="abs field" style="top:507px">Email</div>
<div class="abs field" style="top:534px">Phone</div>
<div class="abs field" style="top:561px;height:53px">Message</div>
<div class="abs btn-submit">Submit</div>

<!-- chirplet feed -->
<div class="abs panel" style="left:586px;top:670px;width:171px;height:147px"></div>
<div class="abs panel-head" style="left:586px;top:670px;width:171px;height:35px">
  <svg width="12" height="10" viewBox="0 0 12 10"><path d="M1 8 6 3M1 4 6 3 5 8" fill="none" stroke="#fff" stroke-width="1.4"/></svg>
  Latest Chirplet
</div>
<div class="abs tw-avatar"></div>
<div class="abs tw-name">Ferncastle System</div>
<div class="abs tw-handle">@ferncastle</div>
<p class="abs tw-text" style="border:0">Lorem ipsum <span>#dolor</span> sit amet, consectet use adipiscing elit. Nunceri non massa utemi ante pelentesque ultricies.</p>
<div class="abs" style="left:599px;top:759px;width:149px;height:1px;background:#eef0f2"></div>

<!-- recent posts -->
<div class="abs panel" style="left:586px;top:829px;width:171px;height:194px"></div>
<div class="abs panel-head" style="left:586px;top:829px;width:171px;height:34px">
  <svg width="9" height="9" viewBox="0 0 9 9"><circle cx="1.5" cy="7.5" r="1.2" fill="#fff"/><path d="M1 4A4 4 0 0 1 5 8M1 1A7 7 0 0 1 8 8" fill="none" stroke="#fff" stroke-width="1.3"/></svg>
  Recent Posts
</div>
<div class="abs post" style="top:880px"><div class="thumb" role="img" aria-label="Post photo"></div><p>Fusce gravida tortor felis, ac<br>tortor felidictum risus sagittis.<b>October 15, 2013</b></p></div>
<div class="abs post" style="top:924px"><div class="thumb" role="img" aria-label="Post photo"></div><p>Fusce gravida tortor felis, ac<br>tortor felidictum risus sagittis.<b>October 15, 2013</b></p></div>
<div class="abs post" style="top:968px"><div class="thumb" role="img" aria-label="Post photo"></div><p>Fusce gravida tortor felis, ac<br>tortor felidictum risus sagittis.<b>October 15, 2013</b></p></div>

<!-- map -->
<div class="abs map" role="img" aria-label="Wendro Map street map showing the office location"></div>

<!-- footer -->
<footer class="abs footer">
  <div class="abs contact-top" style="left:195px;top:10px;color:#9aa3ae">
    <svg width="14" height="9" viewBox="0 0 14 9"><rect x="2" y=".5" width="11" height="8" fill="none" stroke="#4aaae8"/><path d="M2 .5 7.5 5 13 .5" fill="none" stroke="#4aaae8"/></svg>
    info@ferncastlesystems.com
  </div>
  <div class="abs contact-top" style="left:315px;top:10px;color:#9aa3ae">
    <svg width="9" height="9" viewBox="0 0 10 10"><path d="M2 1 4 1 5 3.5 3.6 4.6Q4.8 6.8 6.4 6.4L7.5 5 10 6 10 8Q9 10 6 9 1 7 1 2Z" fill="#4aaae8"/></svg>
    +44 100 555 0199
  </div>
  <div class="abs" style="left:585px;top:11px">Copyright © 2014 Ferncastle Systems. All Rights Reserved</div>
</footer>

</body>
</html>
```